Flyer

I am a qualified accountant and I need a flyer to promote my business when networking

My services include
Management Accounts, Financial Accounts, Day to Day Bookkeeping services, business start up assistance
I will produce and submit Self Assessment Tax Returns, Annual Accounts, VAT tax returns, Payroll and PAYE

I attach my business card design so that there is some continuity if you think it appropiate.

Size A3 is preferred, please.

Sorry, I mean't Size A5 is preferred.

A5 please

Free initial consultations and advice.

```html
<!DOCTYPE html>
<html lang="en">
<head>
<meta charset="utf-8">
<title>Clara Whitmore Accounting – Flyer</title>
<link rel="stylesheet" href="https://fonts.googleapis.com/css2?family=Cinzel:wght@400;500&family=Roboto+Condensed:wght@300;400;700&display=swap">
<style>
  :root {
    --lime: #c2d82f;
    --leaf: #8dc63f;
    --ink: #1f1f1f;
    --forest: #2f7d32;
    --paper: #ffffff;
    --backdrop: #e6e6e6;
  }
  * { margin: 0; padding: 0; box-sizing: border-box; }
  html, body {
    width: 1200px; height: 1200px; overflow: hidden;
    background: var(--backdrop);
  }
  .flyer {
    position: absolute; left: 212px; top: 50px;
    width: 775px; height: 1100px;
    background: var(--paper);
    overflow: hidden;
  }
  .flyer-shapes { position: absolute; inset: 0; width: 100%; height: 100%; }
  .text-block { position: absolute; left: 0; width: 100%; text-align: center; }
  .credential-title {
    top: 36px;
    font-family: "Cinzel", serif; font-weight: 500;
    font-size: 40px; color: var(--ink);
  }
  .service-list {
    top: 200px; list-style: none;
    font-family: "Roboto Condensed", sans-serif; font-weight: 700;
    font-size: 38px; line-height: 48px; color: var(--ink);
  }
  .submission-heading {
    top: 430px;
    font-family: "Roboto Condensed", sans-serif; font-weight: 700;
    font-size: 34px; color: var(--leaf);
  }
  .submission-detail {
    top: 474px;
    font-family: "Roboto Condensed", sans-serif; font-weight: 300;
    font-size: 24px; line-height: 31px; color: var(--ink);
  }
  .brand-name {
    top: 748px;
    font-family: "Roboto Condensed", sans-serif; font-weight: 700;
    font-size: 36px; color: var(--forest);
  }
  .contact-email {
    top: 930px;
    font-family: "Cinzel", serif; font-size: 24px; color: var(--ink);
  }
  .contact-phone {
    top: 964px;
    font-family: "Cinzel", serif; font-size: 32px; color: var(--ink);
  }
  .consultation-offer {
    top: 1038px;
    font-family: "Roboto Condensed", sans-serif; font-weight: 700;
    font-size: 38px; color: var(--paper);
  }
</style>
</head>
<body>
  <main class="flyer">
    <svg class="flyer-shapes" viewBox="0 0 620 880" preserveAspectRatio="none" aria-hidden="true">
      <path d="M0,0 H620 V78 Q310,132 0,78 Z" fill="var(--lime)"/>
      <path d="M0,88 Q310,142 620,88" fill="none" stroke="var(--lime)" stroke-width="3"/>
      <path d="M0,526 Q310,446 620,526" fill="none" stroke="var(--lime)" stroke-width="3"/>
      <path d="M0,536 Q310,456 620,536 V880 H0 Z" fill="var(--lime)"/>
      <path d="M0,766 Q310,880 620,766 V880 H0 Z" fill="var(--leaf)"/>
      <path d="M0,758 Q310,872 620,758" fill="none" stroke="var(--paper)" stroke-width="4"/>
    </svg>

    <h1 class="text-block credential-title">Clara Whitmore ACMA, CGMA</h1>

    <ul class="text-block service-list">
      <li>Management Accounts</li>
      <li>Financial Accounts</li>
      <li>Day to Day Bookkeeping services</li>
      <li>Business Start Up Assistance</li>
    </ul>

    <h2 class="text-block submission-heading">Production and submission of</h2>
    <p class="text-block submission-detail">
      Self Assessment Tax Returns, VAT returns, Annual Accounts,<br>
      Payroll &amp; PAYE<br>
      I also offer business start up assitance
    </p>

    <p class="text-block brand-name">Clara Whitmore Accounting</p>

    <p class="text-block contact-email">CLARA@WHITMOREACCOUNTING.COM</p>
    <p class="text-block contact-phone">07700 900123</p>

    <p class="text-block consultation-offer">Free initial consultations and advice.</p>
  </main>
</body>
</html>
```